k eLiquid Label

We are an electronic cigarette eLiquid manufacturer with an outdated label design which needs to be updated and become more modern. All information listed on the label cannot be changed or removed.

There are 4 colour coding on the labels that cannot change.
0mg is white
12mg is yellow
18mg is blue
24mg is red

We prefer a blue type background however are not committed to it with the proper design however if a new colour is chosen it must compliment the colour band for each colour coding

The "dots" on the front of the bottle need to be larger.

The "V" on the front needs to be in this font however we can accept slight changes to it for effect.

Issues we are facing:
The 0mg and the 18mg look too close in colour and need to be completely different in colouring.

The background colouring is too dark and you cannot see the 50/50 in the watermark.

Reason: We have not received a design which is suitable to our needs. We have see a few close ones however not exact. Thanks

Reason: I was forced to go out of country for a family emergency and to be fair I am extending the deadline

```html
<!DOCTYPE html>
<html lang="en">
<head>
<meta charset="utf-8">
<title>k eLiquid Label – Sweet Tobacco 24 mg/ml</title>
<link href="https://fonts.googleapis.com/css2?family=Arimo:wght@400;700&family=Didact+Gothic&display=swap" rel="stylesheet">
<style>
  :root {
    --page: #e9e9e9;
    --band-red: #e8141b;
    --band-red-dark: #c20d12;
    --band-text: #7a0c10;
    --sky-top: #8fd3f7;
    --sky-mid: #5cc2f2;
    --sky-deep: #3eaee8;
    --ink: #1b2a36;
    --ink-soft: #2e4656;
    --ink-teal: #2d7f9a;
    --pixel: #8e0f14;
    --badge: #e8141b;
    --white: #ffffff;
    --watermark: rgba(255,255,255,0.22);
  }
  * { box-sizing: border-box; margin: 0; padding: 0; }
  html, body { width: 1200px; height: 835px; overflow: hidden; }
  body {
    background: var(--page);
    font-family: "Arimo", Arial, sans-serif;
    display: flex; align-items: center; justify-content: center;
  }
  .label {
    position: relative;
    width: 1120px; height: 420px;
    background: linear-gradient(180deg, var(--sky-top) 0%, var(--sky-mid) 55%, var(--sky-deep) 100%);
    box-shadow: 0 6px 18px rgba(0,0,0,0.18);
    overflow: hidden;
    color: var(--ink);
  }
  .smoke {
    position: absolute; left: 0; right: 0; top: 32px; bottom: 40px;
    background:
      radial-gradient(ellipse 260px 90px at 20% 75%, rgba(255,255,255,0.25), transparent 70%),
      radial-gradient(ellipse 300px 110px at 55% 65%, rgba(255,255,255,0.22), transparent 70%),
      radial-gradient(ellipse 260px 90px at 88% 70%, rgba(255,255,255,0.2), transparent 70%);
  }
  .band {
    position: absolute; left: 0; right: 0;
    background: linear-gradient(180deg, var(--band-red), var(--band-red-dark));
    display: flex; justify-content: space-around; align-items: center;
    font-weight: 700; white-space: nowrap;
  }
  .band--strength { top: 0; height: 32px; font-size: 14px; color: var(--band-text); }
  .band--danger { bottom: 0; height: 40px; font-size: 16px; color: #2a0000; letter-spacing: 0.5px; }
  .watermark {
    position: absolute; left: 450px; top: 60px; width: 300px; text-align: center;
    font-size: 100px; font-weight: 700; line-height: 1;
    color: var(--watermark);
  }
  .column { position: absolute; top: 44px; width: 310px; font-size: 14px; line-height: 1.25; }
  .column--fr { left: 40px; text-align: right; color: var(--ink-soft); }
  .column--en { left: 780px; text-align: left; color: var(--ink-soft); }
  .column h2 { font-size: 14px; font-weight: 700; color: var(--ink-teal); margin-bottom: 2px; }
  .column--en h2 { color: var(--white); }
  .column p { margin-bottom: 10px; }
  .column strong { color: var(--ink); }
  .column .urgent { font-weight: 700; color: #000; font-size: 15px; }
  .hazard { position: absolute; left: 50px; top: 70px; }
  .record {
    display: flex; justify-content: space-between;
    background: var(--white); color: #000; font-weight: 700; font-size: 13px;
    padding: 4px 10px; width: 300px; margin: 0 0 10px 0;
  }
  .record span:last-child { width: 140px; }
  .pixels { position: absolute; background: var(--pixel); opacity: 0.9; }
  .pixels--tl { left: 400px; top: 46px; width: 56px; height: 44px; }
  .pixels--tr { left: 664px; top: 46px; width: 56px; height: 44px; }
  .pixels--bl { left: 428px; top: 296px; width: 56px; height: 56px; }
  .pixels--br { left: 716px; top: 296px; width: 56px; height: 56px; }
  .brand {
    position: absolute; left: 440px; top: 130px; width: 320px;
    display: flex; justify-content: center;
  }
  .brand-name { font-family: "Didact Gothic", Arial, sans-serif; font-size: 58px; color: #222; line-height: 1; }
  .strength-badge {
    position: absolute; left: 672px; top: 205px;
    width: 56px; height: 56px; border-radius: 50%;
    background: var(--badge); color: var(--white);
    display: flex; align-items: center; justify-content: center;
    font-size: 26px; font-weight: 700;
  }
  .flavour {
    position: absolute; left: 495px; top: 302px;
    width: 210px; text-align: center;
    background: var(--band-red); color: var(--white);
    border: 2px solid var(--white); border-radius: 6px;
    font-family: "Didact Gothic", Arial, sans-serif; font-size: 22px; padding: 2px 0;
  }
  .volume { position: absolute; left: 495px; top: 346px; width: 210px; text-align: center; font-size: 13px; color: #333; }
</style>
</head>
<body>
  <article class="label" aria-label="k eLiquid Sweet Tobacco 24 mg/ml label">
    <div class="smoke" role="img" aria-label="Soft drifting smoke in the background"></div>

    <div class="band band--strength">
      <span>24 mg/ml</span><span>24 mg/ml</span><span>24 mg/ml</span><span>24 mg/ml</span><span>24 mg/ml</span><span>24 mg/ml</span><span>24 mg/ml</span><span>24 mg/ml</span><span>24 mg/ml</span><span>24 mg/ml</span>
    </div>

    <div class="watermark" aria-hidden="true">50/50<br>50/50</div>

    <div class="pixels pixels--tl" role="img" aria-label="Red pixel square cluster"></div>
    <div class="pixels pixels--tr" role="img" aria-label="Red pixel square cluster"></div>
    <div class="pixels pixels--bl" role="img" aria-label="Red pixel square cluster"></div>
    <div class="pixels pixels--br" role="img" aria-label="Red pixel square cluster"></div>

    <svg class="hazard" width="50" height="44" viewBox="0 0 50 44" role="img" aria-label="Poison hazard symbol">
      <polygon points="25,2 48,42 2,42" fill="#3a3a3a" stroke="#dfe6ea" stroke-width="2"/>
    </svg>

    <section class="column column--fr" lang="fr">
      <h2>CONTENIR NOCIF</h2>
      <p>Ne pas avaler.<br>Ne pas mettre dans les yeux ou<br>sur la peau ou les vetements.<br>Tenir hors de portee des enfants et<br>des animaux.</p>
      <p><strong>INGREDIENTS:</strong> Propylene Glycol,<br>Glycerine, Alcool de Qualite Alimentaire,<br>Aromes Naturel et Artificiels.</p>
      <p class="urgent">En cas d’ingestion consulter<br>centre antipoison ou un medecin<br>immediatement. Peux contenir de noix.</p>
      <p>Produit et emballe exclusivement pour:<br>4418203 Canada Inc., Millbrook ON<br>K0L 3A1</p>
    </section>

    <div class="brand">
      <span class="brand-name">k eLiquid</span>
    </div>
    <div class="strength-badge">24</div>
    <div class="flavour">SWEET TOBACCO</div>
    <div class="volume">vol. 30ml</div>

    <section class="column column--en">
      <h2>WARNING CONTENTS HARMFUL!</h2>
      <p>Do not swallow.<br>Do not get in eyes or on skin or clothing.<br>Keep out of reach of children and pets.</p>
      <p><strong>INGREDIENTS:</strong> Propylene Glycol,<br>Vegetable GLycerin, Nicotine (1.2%),<br>Food Grade Alcohol, Natural and<br>Artificial Flavours.</p>
      <p class="urgent">If swallowed consult poison control<br>center or a doctor immediately.<br>May contain nuts.</p>
      <div class="record"><span>BATCH:</span><span>EXPIRES:</span></div>
      <p>Produced and Packaged exclusively for:<br>4418203 Canada Inc., Millbrook ON,<br>K0L 3A1</p>
    </section>

    <div class="band band--danger">
      <span>DANGER&nbsp;&nbsp;POISON</span><span>DANGER&nbsp;&nbsp;POISON</span><span>DANGER&nbsp;&nbsp;POISON</span><span>DANGER&nbsp;&nbsp;POISON</span><span>DANGER&nbsp;&nbsp;POISON</span><span>DANGER&nbsp;&nbsp;POISON</span>
    </div>
  </article>
</body>
</html>
```